Kestrim LLC, needs a web page no more than 5 pages (for now)

Kestrim is a general contractor. Our services include general contracting, design-build construction, disaster recovery and environmental remediation. Our main clients are KZE, HJ, State and Local Gov't Agencies, Hospitals and Schools. Kestrim is also a SDVOSB.

```html
<!DOCTYPE html>
<html lang="en">
<head>
<meta charset="UTF-8">
<title>Kestrim LLC</title>
<link href="https://fonts.googleapis.com/css2?family=Montserrat:wght@600;700&family=Open+Sans:ital,wght@0,400;0,600;0,700;1,400&display=swap" rel="stylesheet">
<style>
:root{
  --navy:#1f2938;
  --navy-soft:#2b3646;
  --gold:#d9a22b;
  --page:#f4f7fa;
  --card:#eef2f6;
  --line:#9aa8b8;
  --ink:#1c2532;
  --body:#3c4654;
  --white:#ffffff;
}
*{margin:0;padding:0;box-sizing:border-box}
html,body{width:1200px;height:4358px;overflow:hidden}
body{background:var(--page);font-family:"Open Sans",Arial,sans-serif;color:var(--ink)}
.site-nav{height:60px;background:var(--white);display:flex;align-items:center;padding:0 100px;border-bottom:1px solid #e3e7ec}
.brand{font-family:"Montserrat",Arial,sans-serif;font-weight:700;font-size:19px;color:var(--ink)}
.nav-links{margin-left:auto;display:flex;align-items:center;gap:0;list-style:none}
.nav-links li{font-size:13px;color:#3b4452;margin-left:29px}
.nav-cta{background:var(--gold);color:var(--ink);padding:10px 20px;margin-left:29px;font-size:13px;display:inline-block;height:34px;margin-top:-10px}
.hero-image{height:621px;background:linear-gradient(160deg,#3e4b5c 0%,#4c5a6c 40%,#39475a 70%,#2a3545 100%)}
.hero{height:1428px;background:var(--navy);text-align:center;padding-top:224px}
.hero h1{font-family:"Montserrat",Arial,sans-serif;font-weight:700;font-size:54px;line-height:64px;color:var(--white);width:760px;margin:0 auto;letter-spacing:1px}
.hero p{font-size:18px;line-height:28px;color:#e6eaf0;width:740px;margin:26px auto 0}
.btn-gold{display:inline-block;background:var(--gold);color:var(--ink);font-family:"Montserrat",Arial,sans-serif;font-weight:600;font-size:14px;border:2px solid #e8b648}
.hero .btn-gold{width:230px;height:53px;line-height:49px;margin-top:31px}
.container{width:1000px;margin:0 auto}
.expertise{padding-top:73px}
.section-title{font-family:"Montserrat",Arial,sans-serif;font-weight:700;font-size:39px;color:var(--ink);letter-spacing:.5px}
.expertise .intro{font-size:14px;line-height:24px;color:var(--body);margin-top:6px}
.cards{display:flex;gap:28px;margin-top:12px}
.service-card{width:314px;height:520px;border:2px solid var(--line);background:var(--card);padding:20px 20px 20px;display:flex;flex-direction:column}
.service-card .photo{height:203px}
.service-card h3{font-family:"Montserrat",Arial,sans-serif;font-weight:600;font-size:26px;line-height:32px;margin-top:50px;height:66px;display:flex;align-items:center}
.service-card p{font-size:14px;line-height:24px;color:var(--body);margin-top:14px}
.btn-outline{margin-top:auto;height:44px;border:2px solid var(--ink);text-align:center;line-height:40px;font-family:"Montserrat",Arial,sans-serif;font-weight:600;font-size:13px}
.cta{text-align:center;padding-top:105px}
.cta h2{font-size:39px}
.cta p{font-size:15px;color:var(--body);margin-top:6px}
.cta .btn-gold{width:204px;height:43px;line-height:39px;margin-top:12px;font-size:13px}
.faq{padding-top:105px}
.faq h2{text-align:center}
.faq-list{margin-top:20px}
.faq-item{border:2px solid #c5ced9;background:var(--card);padding:24px 20px;margin-bottom:21px}
.faq-item h3{font-family:"Open Sans",Arial,sans-serif;font-weight:700;font-size:14px;color:var(--ink)}
.faq-item p{font-size:14px;line-height:24px;color:var(--body);margin-top:12px}
.testimonials{padding-top:76px}
.testimonials h2{text-align:center;line-height:42px}
.quotes{display:flex;gap:28px;margin-top:-2px}
.quote-card{width:314px;height:315px;border:2px solid var(--line);background:var(--card);padding:42px 20px 20px;display:flex;flex-direction:column}
.quote-card blockquote{font-style:italic;font-size:14px;line-height:24px;color:var(--body)}
.quote-card .who{margin-top:auto;text-align:right;font-size:14px;line-height:24px;color:var(--ink)}
.quote-card .who strong{display:block;font-weight:700}
.site-footer{position:absolute;top:4249px;left:0;width:1200px;height:109px;background:var(--navy);display:flex;align-items:center;padding:0 100px}
.site-footer small{font-size:14px;color:#b9c2cf}
.footer-links{margin-left:auto;display:flex;gap:22px;list-style:none}
.footer-links li{font-size:12px;color:#b9c2cf}
</style>
</head>
<body>
<header class="site-nav">
  <div class="brand">Kestrim</div>
  <ul class="nav-links">
    <li>Home</li><li>Services</li><li>Projects</li><li>About Us</li><li>SDVOSB</li>
    <li class="nav-cta">Contact</li>
  </ul>
</header>

<div class="hero-image" role="img" aria-label="Dimmed photo of a laptop and a glass on a desk"></div>

<section class="hero">
  <h1>Architectural Brutalist Elegance: Building Trust, Delivering Precision.</h1>
  <p>Kestrim specializes in large-scale, critical construction and remediation projects. Our expertise ensures structural integrity and sophisticated execution for the most demanding clients.</p>
  <span class="btn-gold">Explore Our Services</span>
</section>

<section class="expertise container">
  <h2 class="section-title">Expertise in Critical Infrastructure</h2>
  <p class="intro">At Kestrim, we combine the raw, honest strength of Brutalist design principles with the refined sophistication of luxury execution. This philosophy drives our commitment to trust, authority, and meticulous craftsmanship in every project.</p>
  <div class="cards">
    <article class="service-card">
      <div class="photo" role="img" aria-label="Wooden boardwalk through dune grass toward the sea" style="background:linear-gradient(180deg,#dfe6ea 0%,#7fa7a8 30%,#7c8a5a 60%,#6a6f4c 100%)"></div>
      <h3>General<br>Contracting</h3>
      <p>Comprehensive project management from conception to completion, ensuring seamless delivery and unparalleled quality.</p>
      <div class="btn-outline">Learn More</div>
    </article>
    <article class="service-card">
      <div class="photo" role="img" aria-label="Old stone bridge with statues at dusk" style="background:linear-gradient(180deg,#6e6a70 0%,#7a6468 40%,#3a3638 75%,#252426 100%)"></div>
      <h3>Design-Build<br>Solutions</h3>
      <p>Streamlined processes integrating design and construction under one roof, optimizing efficiency and client collaboration.</p>
      <div class="btn-outline">Learn More</div>
    </article>
    <article class="service-card">
      <div class="photo" role="img" aria-label="Pale misty grey landscape" style="background:linear-gradient(180deg,#e9eaeb 0%,#dcdddf 100%)"></div>
      <h3>Disaster Recovery</h3>
      <p>Rapid response and robust recovery efforts to restore critical infrastructure efficiently and effectively after emergencies.</p>
      <div class="btn-outline">Learn More</div>
    </article>
  </div>
</section>

<section class="cta container">
  <h2 class="section-title">Ready to Build the Future?</h2>
  <p>Partner with Kestrim for projects that demand uncompromising quality and precision.</p>
  <span class="btn-gold">Request a Consultation</span>
</section>

<section class="faq container">
  <h2 class="section-title">Frequently Asked Questions</h2>
  <div class="faq-list">
    <div class="faq-item">
      <h3>What types of projects does Kestrim specialize in?</h3>
      <p>Kestrim specializes in large-scale, critical construction, and remediation projects. Our expertise spans general contracting, design-build solutions, and disaster recovery efforts, focusing on structural integrity and sophisticated execution.</p>
    </div>
    <div class="faq-item">
      <h3>Is Kestrim a Service-Disabled Veteran-Owned Small Business (SDVOSB)?</h3>
      <p>Yes, Kestrim is proud to be a certified Service-Disabled Veteran-Owned Small Business (SDVOSB). We bring the discipline, leadership, and precision gained through military service to every project.</p>
    </div>
    <div class="faq-item">
      <h3>How does Kestrim approach project management?</h3>
      <p>We employ a comprehensive project management approach, integrating design and construction to ensure seamless delivery. Our philosophy is rooted in Architectural Brutalist Elegance, emphasizing trust, authority, and meticulous craftsmanship from conception to completion.</p>
    </div>
    <div class="faq-item">
      <h3>How can I request a consultation?</h3>
      <p>You can request a consultation by visiting our Contact Us page and filling out the inquiry form, or by reaching out to us directly via phone or email.</p>
    </div>
  </div>
</section>

<section class="testimonials container">
  <h2 class="section-title">What Our Clients Say</h2>
  <div class="quotes">
    <article class="quote-card">
      <blockquote>"Kestrim delivered exceptional quality on a highly complex infrastructure project. Their attention to detail and commitment to deadlines were truly impressive. A reliable partner we wholeheartedly recommend."</blockquote>
      <div class="who"><strong>Daniel R.</strong>CEO, Urban Development Group</div>
    </article>
    <article class="quote-card">
      <blockquote>"The team at Kestrim handled our disaster recovery efforts with remarkable efficiency and professionalism. They restored our facilities faster than we thought possible, minimizing disruption."</blockquote>
      <div class="who"><strong>Priya M.</strong>Operations Director, Regional Logistics Hub</div>
    </article>
    <article class="quote-card">
      <blockquote>"We partnered with Kestrim for a design-build initiative, and the collaboration was seamless. Their ability to integrate architectural vision with practical construction expertise is unmatched."</blockquote>
      <div class="who"><strong>Owen L.</strong>Lead Architect, Ridgeline Studios</div>
    </article>
  </div>
</section>

<footer class="site-footer">
  <small>© 2024 Kestrim. All Rights Reserved.</small>
  <ul class="footer-links"><li>Privacy Policy</li><li>Terms of Service</li><li>Sitemap</li></ul>
</footer>
</body>
</html>
```